Power/Telecommunications Contracting Ad

We need an eye catching advertisement that will be posted in magazines and news papers. I am open to all sizes of ad space. It has to have a list of things we do, our contact info and a logo of Velm Accreditation.
We provide:
Telecommunications and High/Low voltage Power Construction
Horizontal Directional Drilling (Trenchless conduit installation)
Vibratory Cable Plowing
Trenching/Excavating for underground utilities
Telecommunications cable splicing
Pole installation and overhead aerial construction
Underground power and telecom cable Installations
Snowcat Services
Located at:
58 Fenwick Lane
Whitehorse Yukon Canada
Y2B 7K9

Contact:
Morris Caskey
President
Morris@brindlenet.example
(867)555-0192

Lionel Caskey
Vice President
Lionel@brindlenet.example
(867)555-0147

Target Market(s)

New clients

Industry/Entity Type

Telecommunications

Requirements
Must have
• Contact info, address, list of services, for certification logo
Nice to have
• I've attatched some pictures of the work we do if you could try to incorporate them into the ad that would be good.

```html
<!DOCTYPE html>
<html lang="en">
<head>
<meta charset="utf-8">
<title>Ridge Run Contracting Inc</title>
<link href="https://fonts.googleapis.com/css2?family=Roboto+Condensed:wght@400;700&display=swap" rel="stylesheet">
<style>
  :root {
    --orange: #f3431b;
    --steel: #8c9296;
    --white: #ffffff;
    --bg-center: #2c2c2c;
    --bg-edge: #0d0d0d;
    --snow: #dfe4ee;
    --sky: #7d8aa6;
  }
  html, body { margin: 0; padding: 0; overflow: hidden; }
  body { width: 960px; height: 1200px; background: var(--bg-edge); }
  .ad {
    position: relative; width: 960px; height: 1200px; overflow: hidden;
    background: radial-gradient(circle at 50% 40%, var(--bg-center) 0%, #1a1a1a 55%, var(--bg-edge) 100%);
    font-family: "Roboto Condensed", "Arial Narrow", sans-serif;
    color: var(--white);
  }
  .brand-ring { position: absolute; left: 340px; top: 24px; }
  .brand-name {
    position: absolute; left: 0; width: 960px; top: 360px; margin: 0;
    text-align: center; font-weight: 700; color: var(--orange);
    line-height: 1; letter-spacing: 2px;
  }
  .brand-name .line-main { display: block; font-size: 84px; }
  .brand-name .line-sub { display: block; font-size: 38px; margin-top: 12px; letter-spacing: 6px; }
  .section-title {
    position: absolute; left: 23px; margin: 0;
    color: var(--orange); font-weight: 700; font-size: 25px; letter-spacing: 0.2px;
  }
  .services-title { top: 509px; }
  .services {
    position: absolute; left: 23px; top: 545px; margin: 0; padding: 0; list-style: none;
    font-size: 25px; line-height: 32px;
  }
  .services li { position: relative; padding-left: 25px; }
  .services li::before {
    content: ""; position: absolute; left: 2px; top: 13px;
    width: 9px; height: 9px; border-radius: 50%; background: var(--orange);
  }
  .contact-title { top: 826px; }
  .person { position: absolute; left: 23px; margin: 0; }
  .person .name { font-size: 31px; font-weight: 700; color: var(--orange); }
  .person .role { font-size: 28px; font-weight: 400; color: var(--white); }
  .person .details { display: block; font-size: 27px; font-weight: 700; margin-top: 4px; }
  .person .sep { color: var(--orange); padding: 0 4px; }
  .person-president { top: 866px; }
  .person-vice { top: 948px; }
  .location-band {
    position: absolute; left: 5px; top: 1051px; width: 950px; height: 144px;
    background: var(--orange);
  }
  .location-label {
    position: absolute; left: 16px; top: 128px; margin: 0;
    transform: rotate(-90deg); transform-origin: 0 0;
    font-size: 18px; font-weight: 400; white-space: nowrap;
  }
  .address {
    position: absolute; left: 55px; top: 16px; margin: 0; font-style: normal;
    font-size: 31px; font-weight: 700; line-height: 40px;
  }
  .accreditation-badge {
    position: absolute; left: 462px; top: 20px; width: 106px; height: 106px;
    border-radius: 50%; background: var(--white);
  }
  .photo {
    position: absolute; width: 300px; height: 300px; border-radius: 50%;
  }
  .photo-tower {
    left: 638px; top: 590px;
    background: linear-gradient(180deg, #6f7a92 0%, #9aa3b8 22%, #4a5564 35%, #c9d1de 55%, var(--snow) 100%);
  }
  .photo-lineman {
    left: 638px; top: 874px;
    background: linear-gradient(180deg, #6d7f94 0%, #a9b5c4 35%, #5b6472 55%, #d3d9e2 80%, #8a919b 100%);
  }
</style>
</head>
<body>
<main class="ad">
  <svg class="brand-ring" width="280" height="280" viewBox="0 0 280 280" aria-hidden="true">
    <circle cx="140" cy="140" r="132" fill="none" stroke="var(--steel)" stroke-width="10"/>
  </svg>

  <h1 class="brand-name">
    <span class="line-main">RIDGE RUN</span>
    <span class="line-sub">CONTRACTING INC</span>
  </h1>

  <h2 class="section-title services-title">WE PROVIDE:</h2>
  <ul class="services">
    <li>Telecommunications and High/Low voltage Power Construction</li>
    <li>Horizontal Directional Drilling (Trenchless conduit installation)</li>
    <li>Vibratory Cable Plowing</li>
    <li>Trenching/Excavating for underground utilities</li>
    <li>Telecommunications cable splicing</li>
    <li>Pole installation and overhead aerial construction</li>
    <li>Underground power and telecom cable Installations</li>
    <li>Snowcat Services</li>
  </ul>

  <h2 class="section-title contact-title">CONTACT:</h2>
  <p class="person person-president">
    <span class="name">MORRIS CASKEY,</span> <span class="role">President</span>
    <span class="details">Morris@brindlenet.example<span class="sep">•</span>(867) 555-0192</span>
  </p>
  <p class="person person-vice">
    <span class="name">LIONEL CASKEY,</span> <span class="role">Vice President</span>
    <span class="details">Lionel@brindlenet.example<span class="sep">•</span>(867) 555-0147</span>
  </p>

  <section class="location-band">
    <p class="location-label">LOCATED AT:</p>
    <address class="address">
      58 Fenwick Lane<br>
      Whitehorse Yukon Canada<br>
      Y2B 7K9
    </address>
    <div class="accreditation-badge" role="img" aria-label="Velm Accreditation badge"></div>
  </section>

  <div class="photo photo-tower" role="img" aria-label="Aerial photo of a telecom tower and equipment shelters on a snowy hilltop"></div>
  <div class="photo photo-lineman" role="img" aria-label="Photo of a lineworker climbing a power pole above a snowy equipment yard"></div>
</main>
</body>
</html>
```